Business card for a shipping supplies business

Needing a business card design. Please see the logo. The logo with the white font should be used if there is a dark background.

We are looking for the following info on the card. Please see the sample info. We will need the info to be changed with a few different employee names and info but all will use the same template.

Business Name: The Crate Heron
Employee Name : Marcus Delaney
Position: Account Manager
Address: 4827 W. Ridge 418 S.
Fort Worth, TX 73948
email: Marcus@thecrateheron.example
telephone: 855-619-2740 x 207
website: www.getparcelkits.example

Target Market(s)

Businesses who ship products for online sales

Industry/Entity Type

Cardboard

Contact Information for Business Card

Name, title, address, website, logo, telephone number

Font styles to use
Sans Serif

Colors
EE7325
F08F49
F5BC92
FAE3D3
FDF4ED

Requirements
Must have
• Logo on back of card. Clean look, just logo, website address

```html
<!DOCTYPE html>
<html lang="en">
<head>
<meta charset="utf-8">
<title>The Crate Heron – Business Card</title>
<link rel="stylesheet" href="https://fonts.googleapis.com/css2?family=Montserrat:wght@400;500;700&display=swap">
<style>
  :root {
    --stage: #2b2b2b;
    --card: #151515;
    --orange: #e8612a;
    --orange-soft: #f08f49;
    --tan: #c98f66;
    --white: #ffffff;
    --muted: #e9e9e9;
  }
  * { box-sizing: border-box; margin: 0; padding: 0; }
  html, body {
    width: 1200px;
    height: 900px;
    overflow: hidden;
    background: var(--stage);
    font-family: "Montserrat", sans-serif;
  }
  .stage {
    width: 1200px;
    height: 900px;
    display: flex;
    flex-direction: column;
    align-items: center;
    justify-content: center;
    gap: 36px;
  }
  .card {
    width: 700px;
    height: 400px;
    background: var(--card);
    border-radius: 4px;
    box-shadow: 0 10px 30px rgba(0,0,0,0.45);
    position: relative;
    overflow: hidden;
  }
  .brand {
    display: flex;
    align-items: center;
    gap: 14px;
  }
  .brand-dot {
    width: 34px;
    height: 34px;
    border-radius: 50%;
    background: var(--orange);
    flex: none;
  }
  .brand-name {
    color: var(--white);
    font-weight: 700;
    font-size: 30px;
    letter-spacing: 1px;
    text-transform: uppercase;
    line-height: 1.1;
  }

  /* Front */
  .card-front .brand {
    position: absolute;
    left: 48px;
    top: 50%;
    transform: translateY(-50%);
    width: 300px;
  }
  .card-front .brand-name { font-size: 26px; }
  .divider {
    position: absolute;
    left: 370px;
    top: 92px;
    width: 2px;
    height: 216px;
    background: var(--orange);
  }
  .contact {
    position: absolute;
    left: 400px;
    top: 100px;
    color: var(--muted);
  }
  .contact-name {
    color: var(--orange);
    font-weight: 700;
    font-size: 22px;
    letter-spacing: 1.5px;
    text-transform: uppercase;
  }
  .contact-title {
    font-size: 15px;
    margin-top: 2px;
    letter-spacing: 0.5px;
  }
  .contact-address {
    font-size: 15px;
    margin-top: 16px;
    line-height: 1.4;
    font-style: normal;
  }
  .contact-lines {
    list-style: none;
    margin-top: 16px;
    font-size: 14px;
    line-height: 1.6;
  }
  .contact-lines li {
    display: flex;
    align-items: center;
    gap: 8px;
  }
  .contact-lines svg {
    width: 12px;
    height: 12px;
    fill: var(--tan);
    flex: none;
  }

  /* Back */
  .card-back {
    display: flex;
    flex-direction: column;
    align-items: center;
    justify-content: center;
    gap: 26px;
  }
  .card-back .brand-name { font-size: 40px; }
  .card-back .brand-dot { width: 46px; height: 46px; }
  .back-web {
    color: var(--muted);
    font-size: 15px;
    letter-spacing: 1px;
  }
</style>
</head>
<body>
<main class="stage">
  <section class="card card-front" aria-label="Business card front">
    <div class="brand">
      <span class="brand-dot"></span>
      <span class="brand-name">The Crate Heron</span>
    </div>
    <div class="divider"></div>
    <div class="contact">
      <h1 class="contact-name">Marcus Delaney</h1>
      <p class="contact-title">Account Manager</p>
      <address class="contact-address">
        4827 W. Ridge 418 S.<br>
        Fort Worth, TX 73948
      </address>
      <ul class="contact-lines">
        <li>
          <svg viewBox="0 0 12 12" aria-hidden="true"><path d="M2.4 0.8l2 2.2-1 1.4c.7 1.6 1.8 2.7 3.4 3.4l1.4-1 2.2 2-1 1.9C5.2 10.5 1.5 6.8.6 1.8z"/></svg>
          855-619-2740 x 207
        </li>
        <li>
          <svg viewBox="0 0 12 12" aria-hidden="true"><path d="M0 2.5h12v7H0z M0.8 3.2L6 7l5.2-3.8" stroke="#151515" stroke-width="0.9"/></svg>
          Marcus@thecrateheron.example
        </li>
        <li>
          <svg viewBox="0 0 12 12" aria-hidden="true"><circle cx="6" cy="6" r="5.5"/><path d="M0.5 6h11M6 0.5c-2.2 3-2.2 8 0 11M6 0.5c2.2 3 2.2 8 0 11" stroke="#151515" stroke-width="0.8" fill="none"/></svg>
          www.getparcelkits.example
        </li>
      </ul>
    </div>
  </section>

  <section class="card card-back" aria-label="Business card back">
    <div class="brand">
      <span class="brand-dot"></span>
      <span class="brand-name">The Crate Heron</span>
    </div>
    <p class="back-web">www.getparcelkits.example</p>
  </section>
</main>
</body>
</html>
```